Now Leasing Banner

Looking for a banner that says the following information approx 4' x 30'

Now Leasing Maplewood Terrace 925-318-6054

Target Market(s)

Drive by traffic

Industry/Entity Type

Residential property management

Requirements
Must have
• Clear and readable from a distance

```html
<!DOCTYPE html>
<html lang="en">
<head>
<meta charset="utf-8">
<title>Now Leasing – Maplewood Terrace</title>
<link rel="stylesheet" href="https://fonts.googleapis.com/css2?family=Orbitron:wght@700;900&display=swap">
<style>
  :root {
    --ink-green: #1b3f1f;
    --field-green: #316b37;
    --lime-accent: #d0e69c;
    --paper: #ffffff;
  }
  html, body {
    margin: 0;
    padding: 0;
    overflow: hidden;
    background: var(--paper);
  }
  .banner {
    display: block;
    width: 1200px;
    height: 160px;
    background: var(--paper);
  }
  .corner-dark { fill: var(--field-green); }
  .corner-light { fill: var(--lime-accent); }
  .headline {
    font-family: "Orbitron", "Arial Black", sans-serif;
    font-weight: 900;
    fill: var(--ink-green);
  }
  .now-word { font-size: 67px; }
  .now-outlined {
    stroke: var(--paper);
    stroke-width: 4px;
    paint-order: stroke;
    stroke-linejoin: miter;
  }
  .leasing-word { font-size: 107px; }
  .property-name { font-size: 56px; }
  .phone-number {
    font-family: "Orbitron", "Arial", sans-serif;
    font-weight: 700;
    font-size: 21px;
    fill: var(--ink-green);
  }
</style>
</head>
<body>
<svg class="banner" viewBox="0 0 1200 160" width="1200" height="160" xmlns="http://www.w3.org/2000/svg">
  <g class="corner-left">
    <polygon class="corner-dark" points="0,0 214,0 0,159"/>
    <polygon class="corner-light" points="214,0 289,0 9,160 0,160"/>
  </g>
  <g class="corner-right">
    <polygon class="corner-light" points="908,0 978,0 1200,160 1192,160"/>
    <polygon class="corner-dark" points="978,0 1200,0 1200,159"/>
  </g>

  <text class="headline now-word" x="83" y="89" textLength="180" lengthAdjust="spacingAndGlyphs"><tspan class="now-outlined">N</tspan>OW</text>
  <text class="headline leasing-word" x="281" y="93" textLength="657" lengthAdjust="spacingAndGlyphs">LEASING</text>
  <text class="headline property-name" x="281" y="148" textLength="657" lengthAdjust="spacingAndGlyphs">MAPLEWOOD TERRACE</text>
  <text class="phone-number" x="945" y="146" textLength="179" lengthAdjust="spacingAndGlyphs">925-318-6054</text>
</svg>
</body>
</html>
```